We are looking to create a graphic that will be used in Facebook posts each week to show the daily Fernvale Bulletin. Attached is an example of what we are looking for. We need to be able to update the forecast. So we will need hi-res vector files. The graphics need to represent the level of mosquito activity: SLIGHT, AVERAGE, INTENSE, EXTREME

```html
<!DOCTYPE html>
<html lang="en">
<head>
<meta charset="utf-8">
<title>Fernvale Bulletin – Weekly Activity Graphic</title>
<link rel="stylesheet" href="https://fonts.googleapis.com/css2?family=Open+Sans:wght@400;600&family=Questrial&family=Montserrat:wght@700&family=Poppins:wght@400;500;600;700&display=swap">
<style>
  :root{
    --page-top:#eee8f0;
    --page-bottom:#e3ebf8;
    --title-olive:#3b4a1f;
    --sub-olive:#5d7d22;
    --field-dark:#2f4a22;
    --field-mid:#5f8a3e;
    --field-light:#c9d8a8;
    --sky:#f6f3e6;
    --headline-green:#22d65c;
    --panel:rgba(246,246,242,0.9);
    --ink:#1c1c1c;
    --muted:#555;
    --divider:#bdbdb8;
    --slight:#1fd41f;
    --average:#fbbb0b;
    --intense:#f24c12;
    --extreme:#a9231b;
    --legend-ink:#333a44;
  }
  *{box-sizing:border-box;margin:0;padding:0}
  html,body{width:1200px;height:1014px;overflow:hidden}
  body{
    background:linear-gradient(160deg,var(--page-top),var(--page-bottom));
    font-family:"Open Sans",sans-serif;
    position:relative;
  }
  .sheet-title{
    position:absolute;top:52px;left:0;width:1200px;text-align:center;
    font-weight:600;font-size:58px;color:var(--title-olive);letter-spacing:0.5px;
  }
  .sheet-subtitle{
    position:absolute;top:125px;left:0;width:1200px;text-align:center;
    font-weight:600;font-size:19px;color:var(--sub-olive);
  }
  .banner{
    position:absolute;left:128px;top:216px;width:944px;height:494px;
    box-shadow:-10px 14px 18px rgba(40,40,60,0.45);
    overflow:hidden;
  }
  .banner-field{
    position:absolute;inset:0;
    background:linear-gradient(180deg,var(--sky) 0%,var(--field-light) 18%,var(--field-mid) 45%,var(--field-dark) 100%);
  }
  .banner-place{
    position:absolute;top:136px;left:0;width:100%;text-align:center;
    font-family:"Questrial",sans-serif;font-size:36px;color:#fff;
  }
  .banner-headline{
    position:absolute;top:180px;left:0;width:100%;text-align:center;
    font-family:"Montserrat",sans-serif;font-weight:700;font-size:70px;
    color:var(--headline-green);letter-spacing:-1px;
  }
  .forecast-panel{
    position:absolute;left:16px;top:274px;width:912px;height:190px;
    background:var(--panel);display:flex;
  }
  .day{
    flex:1;position:relative;display:flex;flex-direction:column;align-items:center;
    padding-top:32px;
    font-family:"Poppins",sans-serif;
  }
  .day + .day::before{
    content:"";position:absolute;left:0;top:14px;bottom:14px;width:1px;background:var(--divider);
  }
  .day-name{font-size:11px;font-weight:500;color:var(--ink)}
  .day-date{font-size:8px;color:var(--muted);margin-top:4px}
  .gauge{width:106px;height:60px;margin-top:30px}
  .level{font-size:7.5px;font-weight:700;margin-top:6px;letter-spacing:0.2px}
  .level.slight{color:var(--slight)}
  .level.average{color:var(--average)}
  .level.intense{color:var(--intense)}
  .level.extreme{color:var(--extreme)}

  .seg{fill:none;stroke-width:13}
  .seg.g{stroke:var(--slight)}
  .seg.y{stroke:var(--average)}
  .seg.o{stroke:var(--intense)}
  .seg.r{stroke:var(--extreme)}
  .rim{fill:none;stroke:var(--ink);stroke-width:2.5}
  .ticks{fill:none;stroke:var(--ink);stroke-width:6}
  .insect{fill:#222}

  .legend-gauge{position:absolute;left:130px;top:758px;width:282px;height:180px}
  .legend-level{
    position:absolute;left:130px;top:954px;width:282px;text-align:center;
    font-size:20px;color:#222;letter-spacing:0.5px;
  }
  .legend-key{
    position:absolute;left:434px;top:840px;font-size:19.5px;color:var(--legend-ink);
  }
  .legend-note{
    position:absolute;left:447px;top:874px;font-size:18px;color:var(--legend-ink);
  }
</style>
</head>
<body>
<svg width="0" height="0" style="position:absolute">
  <defs>
    <g id="gauge-frame">
      <path class="rim" d="M8,72 A62,62 0 0 1 132,72"/>
      <path class="ticks" d="M8,72 A62,62 0 0 1 132,72" pathLength="50" stroke-dasharray="0.35 9.65"/>
      <path class="rim" d="M3,73 H10 M130,73 H137"/>
    </g>
  </defs>
</svg>

<h1 class="sheet-title">Fernvale Bulletin</h1>
<p class="sheet-subtitle">Mockup 1- size 1200X630 px | &nbsp;Vector Format</p>

<section class="banner">
  <div class="banner-field" role="img" aria-label="Photo of a green wheat field against a bright sky"></div>
  <p class="banner-place">Greater Fernvale</p>
  <h2 class="banner-headline">Fernvale Bulletin</h2>

  <div class="forecast-panel">
    <div class="day">
      <span class="day-name">Mon Day</span><span class="day-date">02/20</span>
      <svg class="gauge" viewBox="0 0 140 80">
        <g transform="rotate(180 70 72)">
          <circle class="seg g" cx="70" cy="72" r="46" pathLength="100" stroke-dasharray="9.3 90.7" stroke-dashoffset="0"/>
          <circle class="seg g" cx="70" cy="72" r="46" pathLength="100" stroke-dasharray="9.3 90.7" stroke-dashoffset="-10"/>
          <circle class="seg g" cx="70" cy="72" r="46" pathLength="100" stroke-dasharray="9.3 90.7" stroke-dashoffset="-20"/>
          <circle class="seg g" cx="70" cy="72" r="46" pathLength="100" stroke-dasharray="9.3 90.7" stroke-dashoffset="-30"/>
          <circle class="seg g" cx="70" cy="72" r="46" pathLength="100" stroke-dasharray="9.3 90.7" stroke-dashoffset="-40"/>
        </g>
        <use href="#gauge-frame"/>
        <ellipse class="insect" cx="70" cy="60" rx="13" ry="16" role="img" aria-label="Mosquito silhouette"/>
      </svg>
      <span class="level slight">SLIGHT</span>
    </div>
    <div class="day">
      <span class="day-name">Tues Day</span><span class="day-date">02/21</span>
      <svg class="gauge" viewBox="0 0 140 80">
        <g transform="rotate(180 70 72)">
          <circle class="seg g" cx="70" cy="72" r="46" pathLength="100" stroke-dasharray="9.3 90.7" stroke-dashoffset="0"/>
          <circle class="seg y" cx="70" cy="72" r="46" pathLength="100" stroke-dasharray="9.3 90.7" stroke-dashoffset="-10"/>
          <circle class="seg y" cx="70" cy="72" r="46" pathLength="100" stroke-dasharray="9.3 90.7" stroke-dashoffset="-20"/>
          <circle class="seg y" cx="70" cy="72" r="46" pathLength="100" stroke-dasharray="9.3 90.7" stroke-dashoffset="-30"/>
          <circle class="seg y" cx="70" cy="72" r="46" pathLength="100" stroke-dasharray="9.3 90.7" stroke-dashoffset="-40"/>
        </g>
        <use href="#gauge-frame"/>
        <ellipse class="insect" cx="70" cy="60" rx="13" ry="16" role="img" aria-label="Mosquito silhouette"/>
      </svg>
      <span class="level average">AVERAGE</span>
    </div>
    <div class="day">
      <span class="day-name">Wednes Day</span><span class="day-date">02/22</span>
      <svg class="gauge" viewBox="0 0 140 80">
        <g transform="rotate(180 70 72)">
          <circle class="seg g" cx="70" cy="72" r="46" pathLength="100" stroke-dasharray="9.3 90.7" stroke-dashoffset="0"/>
          <circle class="seg y" cx="70" cy="72" r="46" pathLength="100" stroke-dasharray="9.3 90.7" stroke-dashoffset="-10"/>
          <circle class="seg o" cx="70" cy="72" r="46" pathLength="100" stroke-dasharray="9.3 90.7" stroke-dashoffset="-20"/>
          <circle class="seg o" cx="70" cy="72" r="46" pathLength="100" stroke-dasharray="9.3 90.7" stroke-dashoffset="-30"/>
          <circle class="seg o" cx="70" cy="72" r="46" pathLength="100" stroke-dasharray="9.3 90.7" stroke-dashoffset="-40"/>
        </g>
        <use href="#gauge-frame"/>
        <ellipse class="insect" cx="70" cy="60" rx="13" ry="16" role="img" aria-label="Mosquito silhouette"/>
      </svg>
      <span class="level intense">INTENSE</span>
    </div>
    <div class="day">
      <span class="day-name">Thurs Day</span><span class="day-date">02/23</span>
      <svg class="gauge" viewBox="0 0 140 80">
        <g transform="rotate(180 70 72)">
          <circle class="seg g" cx="70" cy="72" r="46" pathLength="100" stroke-dasharray="9.3 90.7" stroke-dashoffset="0"/>
          <circle class="seg y" cx="70" cy="72" r="46" pathLength="100" stroke-dasharray="9.3 90.7" stroke-dashoffset="-10"/>
          <circle class="seg o" cx="70" cy="72" r="46" pathLength="100" stroke-dasharray="9.3 90.7" stroke-dashoffset="-20"/>
          <circle class="seg r" cx="70" cy="72" r="46" pathLength="100" stroke-dasharray="9.3 90.7" stroke-dashoffset="-30"/>
          <circle class="seg r" cx="70" cy="72" r="46" pathLength="100" stroke-dasharray="9.3 90.7" stroke-dashoffset="-40"/>
        </g>
        <use href="#gauge-frame"/>
        <ellipse class="insect" cx="70" cy="60" rx="13" ry="16" role="img" aria-label="Mosquito silhouette"/>
      </svg>
      <span class="level extreme">EXTREME</span>
    </div>
    <div class="day">
      <span class="day-name">Fri Day Day</span><span class="day-date">02/24</span>
      <svg class="gauge" viewBox="0 0 140 80">
        <g transform="rotate(180 70 72)">
          <circle class="seg g" cx="70" cy="72" r="46" pathLength="100" stroke-dasharray="9.3 90.7" stroke-dashoffset="0"/>
          <circle class="seg g" cx="70" cy="72" r="46" pathLength="100" stroke-dasharray="9.3 90.7" stroke-dashoffset="-10"/>
          <circle class="seg g" cx="70" cy="72" r="46" pathLength="100" stroke-dasharray="9.3 90.7" stroke-dashoffset="-20"/>
          <circle class="seg g" cx="70" cy="72" r="46" pathLength="100" stroke-dasharray="9.3 90.7" stroke-dashoffset="-30"/>
          <circle class="seg g" cx="70" cy="72" r="46" pathLength="100" stroke-dasharray="9.3 90.7" stroke-dashoffset="-40"/>
        </g>
        <use href="#gauge-frame"/>
        <ellipse class="insect" cx="70" cy="60" rx="13" ry="16" role="img" aria-label="Mosquito silhouette"/>
      </svg>
      <span class="level slight">SLIGHT</span>
    </div>
    <div class="day">
      <span class="day-name">Satur Day</span><span class="day-date">02/25</span>
      <svg class="gauge" viewBox="0 0 140 80">
        <g transform="rotate(180 70 72)">
          <circle class="seg g" cx="70" cy="72" r="46" pathLength="100" stroke-dasharray="9.3 90.7" stroke-dashoffset="0"/>
          <circle class="seg y" cx="70" cy="72" r="46" pathLength="100" stroke-dasharray="9.3 90.7" stroke-dashoffset="-10"/>
          <circle class="seg o" cx="70" cy="72" r="46" pathLength="100" stroke-dasharray="9.3 90.7" stroke-dashoffset="-20"/>
          <circle class="seg r" cx="70" cy="72" r="46" pathLength="100" stroke-dasharray="9.3 90.7" stroke-dashoffset="-30"/>
          <circle class="seg r" cx="70" cy="72" r="46" pathLength="100" stroke-dasharray="9.3 90.7" stroke-dashoffset="-40"/>
        </g>
        <use href="#gauge-frame"/>
        <ellipse class="insect" cx="70" cy="60" rx="13" ry="16" role="img" aria-label="Mosquito silhouette"/>
      </svg>
      <span class="level extreme">EXTREME</span>
    </div>
    <div class="day">
      <span class="day-name">Sun Day</span><span class="day-date">02/26</span>
      <svg class="gauge" viewBox="0 0 140 80">
        <g transform="rotate(180 70 72)">
          <circle class="seg g" cx="70" cy="72" r="46" pathLength="100" stroke-dasharray="9.3 90.7" stroke-dashoffset="0"/>
          <circle class="seg y" cx="70" cy="72" r="46" pathLength="100" stroke-dasharray="9.3 90.7" stroke-dashoffset="-10"/>
          <circle class="seg o" cx="70" cy="72" r="46" pathLength="100" stroke-dasharray="9.3 90.7" stroke-dashoffset="-20"/>
          <circle class="seg o" cx="70" cy="72" r="46" pathLength="100" stroke-dasharray="9.3 90.7" stroke-dashoffset="-30"/>
          <circle class="seg o" cx="70" cy="72" r="46" pathLength="100" stroke-dasharray="9.3 90.7" stroke-dashoffset="-40"/>
        </g>
        <use href="#gauge-frame"/>
        <ellipse class="insect" cx="70" cy="60" rx="13" ry="16" role="img" aria-label="Mosquito silhouette"/>
      </svg>
      <span class="level intense">INTENSE</span>
    </div>
  </div>
</section>

<svg class="legend-gauge" viewBox="0 0 140 90">
  <g transform="rotate(180 70 72)">
    <circle class="seg g" cx="70" cy="72" r="50" pathLength="100" stroke-dasharray="7.8 92.2" stroke-dashoffset="0"/>
    <circle class="seg y" cx="70" cy="72" r="50" pathLength="100" stroke-dasharray="7.8 92.2" stroke-dashoffset="-8.33"/>
    <circle class="seg o" cx="70" cy="72" r="50" pathLength="100" stroke-dasharray="7.8 92.2" stroke-dashoffset="-16.67"/>
    <circle class="seg o" cx="70" cy="72" r="50" pathLength="100" stroke-dasharray="7.8 92.2" stroke-dashoffset="-25"/>
    <circle class="seg r" cx="70" cy="72" r="50" pathLength="100" stroke-dasharray="7.8 92.2" stroke-dashoffset="-33.33"/>
    <circle class="seg r" cx="70" cy="72" r="50" pathLength="100" stroke-dasharray="7.8 92.2" stroke-dashoffset="-41.67"/>
  </g>
  <use href="#gauge-frame"/>
  <ellipse class="insect" cx="70" cy="62" rx="16" ry="22" role="img" aria-label="Mosquito silhouette"/>
</svg>
<p class="legend-level">AVERAGE</p>

<p class="legend-key">Slight: Green &nbsp;| &nbsp;Average: Yellow &nbsp;| &nbsp;Intense : Orange &nbsp;| &nbsp;Intense: RED</p>
<p class="legend-note">Slide color can be chnage easily in the deisgn</p>
</body>
</html>
```